Heritage Hollow Business Cards

Require a business card design. <br/><br/>Needs to include logo (either round or long version) plus these details:<br/>Maya Torvel<br/>Heritage Hollow<br/>maya@quonbrook.com.au<br/>02 6481 7390<br/>PO Box Glenwarra NSW 2913<br/>www.heritagehollow.com.au<br/><br/>I need in an editable format so that I can create for multiple staff members. <br/><br/>

Target Market(s)

We are an online store selling renovation products to home owners are builders. Looking for a classic classy design.

Industry/Entity Type

Home And Garden

Contact Information for Business Card

Maya Torvel
Heritage Hollow
maya@quonbrook.com.au
02 6481 7390
PO Box Glenwarra NSW 2913
www.heritagehollow.com.au

Colors

Designer to choose colors to be used in the design.

Requirements
Must have
• Must include Logo.

```html
<!DOCTYPE html>
<html lang="en">
<head>
<meta charset="utf-8">
<title>Heritage Hollow Business Cards</title>
<link rel="stylesheet" href="https://fonts.googleapis.com/css2?family=Roboto:wght@400;500;700&display=swap">
<style>
  :root {
    --backdrop: #d4d4d6;
    --card-dark: #2b2a2a;
    --card-light: #ffffff;
    --ink: #2a2a2a;
    --ink-soft: #4a4a4a;
    --on-dark: #f2f2f2;
  }
  * { box-sizing: border-box; margin: 0; padding: 0; }
  html, body {
    width: 1200px; height: 900px; overflow: hidden;
    background: var(--backdrop);
    font-family: "Roboto", Arial, sans-serif;
  }
  .canvas { position: relative; width: 1200px; height: 900px; }
  .card {
    position: absolute; width: 560px; height: 320px;
    border-radius: 22px;
    box-shadow: 0 6px 18px rgba(0,0,0,0.18);
    overflow: hidden;
  }
  .card--front { left: 90px; top: 100px; background: var(--card-dark); }
  .card--back { left: 550px; top: 470px; background: var(--card-light); color: var(--ink); }

  .brand { display: flex; align-items: center; gap: 16px; }
  .brand__mark { flex: none; border-radius: 50%; }
  .brand__name { font-weight: 400; line-height: 1; white-space: nowrap; }

  .card--front .brand {
    position: absolute; left: 0; right: 0; top: 0; bottom: 0;
    justify-content: center;
  }
  .card--front .brand__mark { width: 78px; height: 78px; border: 2px solid var(--on-dark); }
  .card--front .brand__name { color: var(--on-dark); font-size: 42px; }

  .card--back .brand { position: absolute; right: 34px; top: 36px; gap: 12px; }
  .card--back .brand__mark { width: 54px; height: 54px; border: 1.5px solid var(--ink); }
  .card--back .brand__name { color: var(--ink); font-size: 22px; }

  .edge-tab {
    position: absolute; left: 0; top: 168px; width: 14px; height: 28px;
    background: var(--card-dark); border-radius: 0 6px 6px 0;
  }

  .holder { position: absolute; left: 42px; top: 140px; }
  .holder__name { font-size: 19px; font-weight: 700; }
  .holder__company { font-size: 12.5px; font-weight: 500; color: var(--ink-soft); margin: 2px 0 0 12px; }

  .contacts { position: absolute; left: 62px; top: 196px; list-style: none; }
  .contacts li { display: flex; align-items: center; gap: 8px; font-size: 14px; color: var(--ink-soft); height: 20px; }
  .contacts svg { width: 13px; height: 13px; fill: var(--ink); flex: none; }

  .divider { position: absolute; left: 56px; right: 34px; top: 262px; height: 1.5px; background: var(--ink); }

  .address { position: absolute; left: 62px; top: 274px; display: flex; align-items: center; gap: 8px; font-size: 14px; color: var(--ink-soft); }
  .address svg { width: 12px; height: 16px; fill: var(--ink); }
</style>
</head>
<body>
<main class="canvas">
  <section class="card card--front">
    <div class="brand">
      <span class="brand__mark"></span>
      <span class="brand__name">Heritage Hollow</span>
    </div>
  </section>

  <section class="card card--back">
    <div class="brand">
      <span class="brand__mark"></span>
      <span class="brand__name">Heritage Hollow</span>
    </div>

    <span class="edge-tab"></span>

    <div class="holder">
      <p class="holder__name">Maya Torvel</p>
      <p class="holder__company">Heritage Hollow</p>
    </div>

    <ul class="contacts">
      <li>
        <svg viewBox="0 0 16 16" aria-hidden="true"><path d="M3 1h3l1 4-2 1c1 2 3 4 5 5l1-2 4 1v3c0 1-1 2-2 2C7 15 1 9 1 3c0-1 1-2 2-2z"/></svg>
        02 6481 7390
      </li>
      <li>
        <svg viewBox="0 0 16 16" aria-hidden="true"><path d="M1 3h14v10H1z M2 4l6 5 6-5" fill="none" stroke="#2a2a2a" stroke-width="1.6"/></svg>
        maya@quonbrook.com.au
      </li>
      <li>
        <svg viewBox="0 0 16 16" aria-hidden="true"><circle cx="8" cy="8" r="6.5" fill="none" stroke="#2a2a2a" stroke-width="1.5"/><path d="M1.5 8h13M8 1.5c-3 3-3 10 0 13M8 1.5c3 3 3 10 0 13" fill="none" stroke="#2a2a2a" stroke-width="1.2"/></svg>
        www.heritagehollow.com.au
      </li>
    </ul>

    <div class="divider"></div>

    <p class="address">
      <svg viewBox="0 0 12 16" aria-hidden="true"><path d="M6 0a6 6 0 0 0-6 6c0 4 6 10 6 10s6-6 6-10a6 6 0 0 0-6-6zm0 8.5A2.5 2.5 0 1 1 6 3.5a2.5 2.5 0 0 1 0 5z"/></svg>
      PO Box Glenwarra NSW 2913
    </p>
  </section>
</main>
</body>
</html>
```